Gilt Corner Shop Sign

Name of company
Gilt Corner
Gilt Corner is a picture framing shop and art gallery selling custom frames, art work and gifts.
Needing a design for shop front sign.

The Sign
The sign is above the shop front window and is approximately 12 feet wide by 43 inches high. White on black. White striped boarder that looks like a picture frame with Gilt Corner in classic lettering including space for a phone number and it may or may not need to include description of services. Something cute in one area like a picture frame with a heart inside. A friendly feel like something that would be special and feels like yours. I have attached a photo of the existing sign to be replaced.

Thank you for your time.

```html
<!DOCTYPE html>
<html lang="en">
<head>
<meta charset="UTF-8">
<title>Gilt Corner Shop Sign</title>
<link href="https://fonts.googleapis.com/css2?family=Cinzel:wght@400;500&family=Marcellus&display=swap" rel="stylesheet">
<style>
  :root {
    --backdrop: #e9e7e4;
    --sign-black: #1b1b1d;
    --sign-ink: #f1e8e6;
  }
  * { margin: 0; padding: 0; box-sizing: border-box; }
  html, body {
    width: 1200px;
    height: 1079px;
    overflow: hidden;
    background: var(--backdrop);
  }
  .canvas {
    position: relative;
    width: 1200px;
    height: 1079px;
    display: flex;
    align-items: center;
    justify-content: center;
  }
  .shop-sign {
    position: relative;
    width: 1120px;
    height: 335px;
    background: var(--sign-black);
    color: var(--sign-ink);
  }
  .frame-line {
    position: absolute;
    border: 2px solid var(--sign-ink);
    pointer-events: none;
  }
  .frame-line--outer { inset: 12px; }
  .frame-line--inner { inset: 20px; border-width: 1.5px; }
  .brand-mark {
    position: absolute;
    left: 58px;
    top: 98px;
    width: 142px;
    height: 152px;
    border: 3px solid var(--sign-ink);
  }
  .shop-name {
    position: absolute;
    left: 238px;
    top: 62px;
    font-family: "Cinzel", serif;
    font-weight: 400;
    font-size: 108px;
    line-height: 1;
    letter-spacing: 2px;
    white-space: nowrap;
  }
  .services {
    position: absolute;
    left: 242px;
    top: 188px;
    font-family: "Cinzel", serif;
    font-weight: 400;
    font-size: 50px;
    line-height: 1;
    letter-spacing: 6px;
    white-space: nowrap;
  }
  .phone {
    position: absolute;
    right: 60px;
    bottom: 44px;
    font-family: "Marcellus", serif;
    font-size: 32px;
    letter-spacing: 0.5px;
    white-space: nowrap;
  }
</style>
</head>
<body>
  <main class="canvas">
    <section class="shop-sign" aria-label="Gilt Corner shop front sign">
      <div class="frame-line frame-line--outer"></div>
      <div class="frame-line frame-line--inner"></div>
      <div class="brand-mark" aria-hidden="true"></div>
      <h1 class="shop-name">Gilt Corner</h1>
      <p class="services">Custom Framing &amp; Art</p>
      <p class="phone">T:01632 960418</p>
    </section>
  </main>
</body>
</html>
```